Business card design for Automotive workshop

We need a business card for a new automotive repair and tyre shop called Ridgeback Prime Automotive located in New Zealand. We are a clean, modern and fresh workshop and company.

Front needs to feature logo,
my name:
Lachie Westergaard (director)

Address:
48 Marlow Lane
Kaimara Bay 3592

Phone: 07 842 1937
Mobile: 027 519 2764
Email: office@ridgebackmotors.co.nz
Website: ridgebackmotors.co.nz

Back needs to feature an area to write down appointment details, date and time.

Also feature a list of jobs and work we do such as,
Vehicle Servicing
All Mechanical Repairs
Warrant of Fitness
Tyres & Wheel Alignments
Automotive Diagnostics
Automotive Parts & Supplies

```html
<!DOCTYPE html>
<html lang="en">
<head>
<meta charset="utf-8">
<title>Ridgeback Prime Automotive – Business Card</title>
<link rel="stylesheet" href="https://fonts.googleapis.com/css2?family=Lato:wght@400;700;900&display=swap">
<style>
  :root {
    --bg: #dedede;
    --card: #ffffff;
    --red: #e3141f;
    --black: #0b0b0b;
    --grey: #8a8a8a;
    --line: #9a9a9a;
  }
  * { margin: 0; padding: 0; box-sizing: border-box; }
  html, body { width: 1200px; height: 960px; overflow: hidden; }
  body {
    background: var(--bg);
    font-family: "Lato", sans-serif;
    position: relative;
  }
  .card {
    position: absolute;
    left: 281px;
    width: 655px;
    height: 375px;
    background: var(--card);
    border-radius: 24px;
    overflow: hidden;
    box-shadow: 0 3px 4px rgba(0,0,0,0.35);
  }
  .card--front { top: 80px; }
  .card--back { top: 506px; }

  .brand {
    position: absolute;
    color: var(--red);
    font-weight: 900;
    font-size: 24px;
    letter-spacing: 1px;
    text-transform: uppercase;
    white-space: nowrap;
    line-height: 1;
  }
  .card--front .brand { top: 78px; left: 0; width: 100%; text-align: center; }
  .card--back .brand { top: 60px; left: 58px; }

  .person { position: absolute; top: 188px; width: 100%; text-align: center; }
  .person__name { color: var(--red); font-weight: 700; font-size: 24px; line-height: 1.1; }
  .person__role { color: var(--grey); font-size: 18px; margin-top: 2px; }

  .contacts {
    position: absolute; top: 270px; width: 100%;
    text-align: center; color: var(--grey); font-size: 17.5px; line-height: 24px;
  }
  .contacts__item { display: inline-flex; align-items: center; gap: 5px; margin: 0 4px; white-space: nowrap; }
  .contacts__item svg { width: 14px; height: 14px; fill: var(--red); }

  .band__stripe { position: absolute; background: var(--black); }
  .band__stripe--l1 { left: 0; width: 186px; top: 337px; height: 12px; }
  .band__stripe--l2 { left: 0; width: 186px; top: 361px; height: 14px; }
  .band__stripe--r1 { left: 466px; right: 0; top: 337px; height: 12px; }
  .band__stripe--r2 { left: 466px; right: 0; top: 361px; height: 14px; }
  .band__address {
    position: absolute; left: 191px; width: 268px; top: 335px; height: 40px;
    background: var(--red); color: #fff; font-size: 17px;
    display: flex; align-items: center; justify-content: center; white-space: nowrap;
  }

  .appt__title { position: absolute; top: 136px; left: 63px; font-size: 25px; font-weight: 700; color: var(--black); }
  .appt__label { position: absolute; color: var(--grey); font-size: 17.5px; }
  .appt__rule { position: absolute; height: 1px; background: var(--line); }

  .services {
    position: absolute; top: 262px; left: 63px; width: 560px;
    list-style: none; color: var(--grey); font-size: 17.5px; line-height: 23.5px;
  }
  .services li { display: inline-flex; align-items: center; margin-right: 6px; white-space: nowrap; }
  .services li::before {
    content: ""; width: 11px; height: 11px; border: 2px solid var(--red); margin-right: 11px;
  }
</style>
</head>
<body>

<section class="card card--front">
  <div class="brand">Ridgeback Prime Automotive</div>

  <div class="person">
    <div class="person__name">Lachie Westergaard</div>
    <div class="person__role">Director</div>
  </div>

  <div class="contacts">
    <span class="contacts__item">
      <svg viewBox="0 0 16 16"><path d="M3 1l3 3-1.5 2c1 2 3 4 5 5l2-1.5 3 3-2 2C6 14 2 10 1 3z"/></svg>07 842 1937
    </span>
    <span class="contacts__item">
      <svg viewBox="0 0 16 16"><path d="M4 0h8v16H4zM5.5 2v10h5V2zM7 13h2v1.5H7z" fill-rule="evenodd"/></svg>027 519 2764
    </span>
    <span class="contacts__item">
      <svg viewBox="0 0 16 16"><path d="M1 3h14v10H1zM2 4l6 5 6-5z" fill-rule="evenodd"/></svg>office@ridgebackmotors.co.nz
    </span>
    <br>
    <span class="contacts__item">
      <svg viewBox="0 0 16 16"><path d="M8 1a7 7 0 1 0 0 14A7 7 0 0 0 8 1zm0 1.5c.8.8 1.4 2.1 1.6 3.5H6.4C6.6 4.6 7.2 3.3 8 2.5zM2.6 7h2.8a10 10 0 0 0 0 2H2.6a5.5 5.5 0 0 1 0-2zm4 0h2.8a9 9 0 0 1 0 2H6.6a9 9 0 0 1 0-2zm4 0h2.8a5.5 5.5 0 0 1 0 2h-2.8a10 10 0 0 0 0-2zM6.4 10h3.2c-.2 1.4-.8 2.7-1.6 3.5-.8-.8-1.4-2.1-1.6-3.5z"/></svg>www.ridgebackmotors.co.nz
    </span>
  </div>

  <div class="band">
    <span class="band__stripe band__stripe--l1"></span>
    <span class="band__stripe band__stripe--l2"></span>
    <span class="band__stripe band__stripe--r1"></span>
    <span class="band__stripe band__stripe--r2"></span>
    <div class="band__address">48 Marlow Lane, Kaimara Bay 3592</div>
  </div>
</section>

<section class="card card--back">
  <div class="brand">Ridgeback Prime Automotive</div>

  <h2 class="appt__title">Appointment</h2>
  <span class="appt__label" style="left:62px; top:186px;">Name :</span>
  <span class="appt__rule" style="left:126px; width:463px; top:206px;"></span>
  <span class="appt__label" style="left:62px; top:222px;">Date&nbsp;&nbsp; :</span>
  <span class="appt__rule" style="left:126px; width:180px; top:242px;"></span>
  <span class="appt__label" style="left:312px; top:222px;">Time&nbsp; :</span>
  <span class="appt__rule" style="left:376px; width:211px; top:242px;"></span>

  <ul class="services">
    <li>Vehicle Servicing</li>
    <li>All Mechanical Repairs</li>
    <li>Warrant of Fitness</li>
    <li>Tyres &amp; Wheel Alignments</li>
    <li>Automotive Diagnostics</li>
    <li>Automotive Parts &amp; Supplies</li>
  </ul>
</section>

</body>
</html>
```